Email Notification & Marketing Templates

I want to start with something like a newsletter or informational email, but i need Top Tips to Detect Phishing Scams. Something that i can send to users so they can follow it when receiving or exchanging emails. I will also need promotional items for my company that i can send to customers as well. It can be based on on our website QRVLINK.COM

Will also need:
newsletters
announcements
marketing emails
alerts
security notifications

Examples:Items such as Security Awareness Poster Series
Phishing Awareness
Password Security
Email Attachments
QR Code scams
Public WiFi safety

```html
<!DOCTYPE html>
<html lang="en">
<head>
<meta charset="utf-8">
<title>Top Tips to Detect Phishing Emails</title>
<link href="https://fonts.googleapis.com/css2?family=Inter:wght@400;500;700;800;900&display=swap" rel="stylesheet">
<style>
  :root {
    --bg: #0a0b0a;
    --bg-soft: #1a1d1a;
    --green: #8ee03a;
    --green-deep: #3f9d16;
    --white: #ffffff;
    --text: #f2f2f2;
    --line: #7fd63a;
  }
  * { margin: 0; padding: 0; box-sizing: border-box; }
  html, body { width: 717px; height: 1200px; overflow: hidden; background: var(--bg); }
  body { font-family: "Inter", Arial, sans-serif; color: var(--text); }
  .poster {
    position: relative; width: 717px; height: 1200px; overflow: hidden;
    background:
      radial-gradient(ellipse 260px 420px at 40px 260px, rgba(70,110,50,0.35), transparent 70%),
      radial-gradient(ellipse 240px 380px at 690px 700px, rgba(90,100,90,0.28), transparent 70%),
      radial-gradient(ellipse 300px 200px at 300px 60px, rgba(60,70,60,0.25), transparent 70%),
      var(--bg);
  }
  .abs { position: absolute; }
  .brand { top: 40px; left: 0; width: 717px; text-align: center; }
  .brand-name { font-size: 64px; font-weight: 900; color: var(--green); line-height: 1; letter-spacing: 1px; }
  .brand-sub { margin-top: 8px; font-size: 13px; font-weight: 500; color: var(--green); letter-spacing: 1.5px; }
  .headline { left: 0; width: 717px; text-align: center; font-weight: 800; line-height: 1; }
  .headline-top { top: 160px; font-size: 39px; color: var(--white); }
  .headline-main { top: 212px; font-size: 57px; color: var(--white); }
  .headline-main .accent { color: var(--green); }
  .intro { top: 302px; left: 0; width: 717px; text-align: center; font-size: 19.5px; line-height: 30px; color: var(--text); }
  .intro .accent { color: var(--green); }
  .grid-line-v { left: 374px; top: 412px; width: 2px; height: 502px; background: var(--line); box-shadow: 0 0 8px var(--line); }
  .grid-line-h { left: 34px; width: 649px; height: 2px; background: var(--line); box-shadow: 0 0 8px var(--line); }
  .tip-icon { width: 42px; height: 42px; }
  .tip-title { font-size: 18px; font-weight: 700; color: var(--green); line-height: 28px; }
  .tip-body { font-size: 16px; line-height: 23px; color: var(--text); }
  .callout { top: 983px; left: 0; width: 717px; padding-left: 24px; text-align: center; font-size: 24px; font-weight: 800; color: var(--green); }
  .tagline { top: 1044px; left: 0; width: 717px; text-align: center; font-size: 21px; color: var(--white); }
  .contact-dot { width: 36px; height: 36px; border-radius: 50%; background: linear-gradient(135deg, var(--green), var(--green-deep)); }
  .contact-text { top: 1113px; font-size: 18px; color: var(--white); }
</style>
</head>
<body>
<main class="poster">
  <header class="abs brand">
    <div class="brand-name">QRV</div>
    <div class="brand-sub">QRV LINK NETWORKS</div>
  </header>

  <h1 class="abs headline headline-top">TOP TIPS TO DETECT</h1>
  <h2 class="abs headline headline-main"><span class="accent">PHISHING</span> EMAILS</h2>
  <p class="abs intro">Protect your organization from cyber threats by following<br>these tips <span class="accent">to detect phishing scams.</span></p>

  <div class="abs grid-line-v"></div>
  <div class="abs grid-line-h" style="top:565px"></div>
  <div class="abs grid-line-h" style="top:728px"></div>

  <svg width="0" height="0" style="position:absolute">
    <defs>
      <linearGradient id="iconFill" x1="0" y1="0" x2="1" y2="1">
        <stop offset="0" stop-color="#a6ee4c"/>
        <stop offset="1" stop-color="#3f9d16"/>
      </linearGradient>
    </defs>
  </svg>

  <!-- Check the sender -->
  <svg class="abs tip-icon" style="left:42px;top:448px" viewBox="0 0 42 42">
    <rect x="1" y="16" width="40" height="25" rx="3" fill="url(#iconFill)"/>
    <path d="M2 18 L21 31 L40 18" fill="none" stroke="#0a0b0a" stroke-width="2"/>
    <circle cx="15" cy="7" r="5" fill="url(#iconFill)"/>
    <path d="M27 12 L27 2 M23 6 L27 2 L31 6" stroke="#8ee03a" stroke-width="2.5" fill="none"/>
  </svg>
  <div class="abs tip-title" style="left:119px;top:447px">CHECK THE SENDER</div>
  <div class="abs tip-body" style="left:119px;top:491px">Verify the sender’s email<br>address carrefully.</div>

  <!-- Pause before you click -->
  <svg class="abs tip-icon" style="left:394px;top:436px" viewBox="0 0 42 42">
    <rect x="7" y="2" width="28" height="16" rx="2" fill="url(#iconFill)"/>
    <circle cx="21" cy="10" r="4" fill="#0a0b0a"/>
    <rect x="1" y="16" width="40" height="24" rx="3" fill="url(#iconFill)"/>
    <path d="M2 18 L21 30 L40 18" fill="none" stroke="#0a0b0a" stroke-width="2"/>
  </svg>
  <div class="abs tip-title" style="left:460px;top:428px">PAUSE BEFORE<br>YOU CLICK</div>
  <div class="abs tip-body" style="left:460px;top:495px">Verify the sender’s email<br>address carrefully.</div>

  <!-- Beware of urgent requests -->
  <svg class="abs tip-icon" style="left:42px;top:598px" viewBox="0 0 42 42">
    <rect x="2" y="2" width="28" height="38" rx="2" fill="url(#iconFill)"/>
    <path d="M7 11 l3 3 5-6 M7 21 l3 3 5-6 M7 31 l3 3 5-6" stroke="#0a0b0a" stroke-width="2" fill="none"/>
    <path d="M19 12 h8 M19 22 h8 M19 32 h8" stroke="#0a0b0a" stroke-width="2"/>
    <rect x="33" y="4" width="6" height="30" fill="url(#iconFill)"/>
    <path d="M33 34 L36 41 L39 34 Z" fill="#8ee03a"/>
  </svg>
  <div class="abs tip-title" style="left:119px;top:590px">BEWARE OF URGENT<br>REQUESTS</div>
  <div class="abs tip-body" style="left:119px;top:656px">Phishing emails often<br>create a sense of urgency.</div>

  <!-- Look for spoofing -->
  <svg class="abs tip-icon" style="left:394px;top:596px" viewBox="0 0 42 42">
    <path d="M8 2 H30 L38 10 V36 H8 Z" fill="url(#iconFill)"/>
    <path d="M14 14 h18 M14 20 h18 M14 26 h12" stroke="#0a0b0a" stroke-width="2"/>
    <circle cx="10" cy="33" r="8" fill="#8ee03a" stroke="#0a0b0a" stroke-width="2"/>
    <path d="M6 33 l3 3 5-6" stroke="#0a0b0a" stroke-width="2" fill="none"/>
  </svg>
  <div class="abs tip-title" style="left:460px;top:603px">LOOK FOR SPOOFING</div>
  <div class="abs tip-body" style="left:460px;top:647px">Watch for misspelled URLs<br>and face websites.</div>

  <!-- Spot poor grammar -->
  <svg class="abs tip-icon" style="left:42px;top:766px" viewBox="0 0 42 42">
    <rect x="17" y="0" width="8" height="8" rx="2" fill="url(#iconFill)"/>
    <rect x="1" y="7" width="40" height="30" rx="3" fill="url(#iconFill)"/>
    <circle cx="12" cy="19" r="4" fill="#0a0b0a"/>
    <path d="M5 31 q7 -9 14 0" fill="#0a0b0a"/>
    <path d="M22 17 h14 M22 23 h10" stroke="#0a0b0a" stroke-width="2"/>
    <circle cx="33" cy="34" r="7" fill="#8ee03a" stroke="#0a0b0a" stroke-width="2"/>
    <path d="M30 34 l2 2 4-4" stroke="#0a0b0a" stroke-width="2" fill="none"/>
  </svg>
  <div class="abs tip-title" style="left:119px;top:769px">SPOT POOR GRAMMAR</div>
  <div class="abs tip-body" style="left:119px;top:812px">Phishing emails oftten have<br>spelling errors</div>

  <!-- Don't share sensitive info -->
  <svg class="abs tip-icon" style="left:394px;top:766px" viewBox="0 0 42 42">
    <path d="M2 4 H28 V24 H12 L5 30 V24 H2 Z" fill="url(#iconFill)"/>
    <path d="M16 14 H40 V34 H37 V40 L31 34 H16 Z" fill="#8ee03a" stroke="#0a0b0a" stroke-width="2"/>
    <circle cx="15" cy="9" r="1.8" fill="#0a0b0a"/>
    <path d="M15 13 v7" stroke="#0a0b0a" stroke-width="2.5"/>
  </svg>
  <div class="abs tip-title" style="left:460px;top:761px">DON’T SHARE<br>SENSITIVE INFO</div>
  <div class="abs tip-body" style="left:460px;top:828px">Never give out passwords or<br>personal details</div>

  <div class="abs callout">WHEN IN DOUBT, REPORT IT !</div>
  <div class="abs tagline">Stay Vigilant. Stay Safe.</div>

  <div class="abs contact-dot" style="left:100px;top:1105px"></div>
  <div class="abs contact-text" style="left:148px">QRVLINK.COM</div>
  <svg class="abs" style="left:333px;top:1104px" width="38" height="38" viewBox="0 0 38 38">
    <circle cx="19" cy="19" r="19" fill="url(#iconFill)"/>
    <path d="M12 10 l4 -1 2 5 -2.5 2 q2 4 5.5 6.5 l2 -2.5 5 2 -1 4 q-2 2 -6 0 q-7 -4 -10 -11 q-1 -3 1 -5z" fill="#0a0b0a"/>
  </svg>
  <div class="abs contact-text" style="left:381px">800-555-0148</div>
  <div class="abs contact-dot" style="left:530px;top:1105px"></div>
  <div class="abs contact-dot" style="left:576px;top:1105px"></div>
</main>
</body>
</html>
```